Pell Roving needs a flashy flyer to capture new clients.

We need a flyer to send out to potential clients that showcases what we do. We are a small business that repairs heavy equipment on site or at our shop. We would like to see the flyer with black and gray colors.

Target Market(s)

New potential clients.

Industry/Entity Type

Mechanic

Font styles to use
Sans Serif

Colors

Designer to choose only greyscale colors for use in the design.

Requirements
Must have
• Telephone number 801-362-5817
Service area Utah, Wyoming, Idaho, Nevada
"Brands we work on Images Below"
24/7 Emergency Service

https://www.findexample.test/search?
q=Pell+Roving+Equipment+Service+%26+Repair&oq=pell
Nice to have
• What We Do:
Mobile On Site Equipment Repair
Preventative Maintenance
Comprehensive Diagnostics
Diesel & Gas Engine Repair
Air Conditioning Systems
Welding & Fabrication
Hydraulic Cylinder & Hose Repair
Pre Purchase Inspections
Annual WSRB Inspections
Pre Purchase Inspections
Should not have
• Open to see some options

```html
<!DOCTYPE html>
<html lang="en">
<head>
<meta charset="UTF-8">
<title>Pell Roving – Mobile Equipment Service & Repair</title>
<link href="https://fonts.googleapis.com/css2?family=Orbitron:wght@800;900&family=Poppins:wght@500;600&family=Russo+One&display=swap" rel="stylesheet">
<style>
  :root {
    --page: #e4e4e4;
    --ink: #0a0a0c;
    --panel: #161616;
    --white: #ffffff;
    --silver-light: #f2f2f2;
    --silver-mid: #9a9a9a;
    --silver-dark: #3a3a3a;
  }
  * { margin: 0; padding: 0; box-sizing: border-box; }
  html, body { width: 1200px; height: 1200px; overflow: hidden; }
  body { background: var(--page); position: relative; font-family: "Poppins", sans-serif; }

  .flyer {
    position: absolute; left: 250px; top: 105px;
    width: 700px; height: 990px;
    background: var(--panel);
    overflow: hidden;
  }
  .flyer-frame { position: absolute; inset: 0; }

  .brand {
    position: absolute; right: 48px; top: 62px;
    text-align: right;
  }
  .brand-name {
    font-family: "Poppins", sans-serif; font-weight: 600;
    font-size: 34px; line-height: 1; letter-spacing: 1px; color: #b4b4b4;
  }
  .brand-tagline {
    font-family: "Poppins", sans-serif; font-weight: 600;
    font-size: 8.5px; letter-spacing: 1.6px; color: #c8c8c8; margin-top: 4px;
  }
  .emergency {
    margin-top: 9px;
    font-family: "Russo One", sans-serif;
    font-size: 12px; letter-spacing: 1.5px; color: var(--white);
  }

  .headline {
    position: absolute; left: 0; width: 700px; top: 440px;
    text-align: center;
    font-family: "Russo One", sans-serif;
    font-size: 38px; letter-spacing: 2px;
    transform: skewX(-10deg);
    background: linear-gradient(180deg, #ffffff 0%, #d9d9d9 45%, #8c8c8c 60%, #e8e8e8 100%);
    -webkit-background-clip: text; background-clip: text; color: transparent;
  }
  .subline {
    position: absolute; left: 0; width: 700px; top: 495px;
    text-align: center;
    font-family: "Russo One", sans-serif;
    font-size: 19px; letter-spacing: 1px; color: #e6e6e6;
    transform: skewX(-10deg);
  }

  .gallery { position: absolute; top: 545px; left: 41px; width: 620px; height: 130px; }
  .gallery-item {
    position: absolute; top: 0; width: 202px; height: 130px;
    border: 2px solid var(--white); border-radius: 6px;
    transform: skewX(-10deg);
  }
  .gallery-item.truck { left: 12px; background: linear-gradient(160deg, #c9cbcd, #eceeef 55%, #8a8d90); }
  .gallery-item.loader { left: 222px; background: linear-gradient(160deg, #6a6d70, #3b3c3a 55%, #8b8a6a); }
  .gallery-item.rig { left: 431px; background: linear-gradient(180deg, #a9c4de 0%, #8a8468 40%, #b9a288 100%); }

  .services-title {
    position: absolute; top: 695px; left: 0; width: 700px;
    display: flex; align-items: center; justify-content: center; gap: 18px;
    color: var(--white); font-weight: 500; font-size: 25px;
  }
  .services-title .rule { width: 180px; height: 2px; background: linear-gradient(90deg, transparent, #ffffff); }
  .services-title .rule.right { background: linear-gradient(90deg, #ffffff, transparent); }

  .services {
    position: absolute; left: 0; width: 700px; list-style: none;
    display: flex; justify-content: center;
    color: var(--white); font-weight: 600; font-size: 14px;
  }
  .services li + li::before { content: "|"; margin: 0 12px; }
  .services.row-1 { top: 737px; }
  .services.row-2 { top: 772px; }
  .services.row-3 { top: 807px; }

  .brands {
    position: absolute; left: 40px; top: 842px; width: 330px;
  }
  .brands-title {
    font-weight: 600; font-size: 11px; letter-spacing: 1px;
    color: #cfcfcf; text-transform: uppercase;
  }
  .brands-row { display: flex; gap: 8px; margin-top: 6px; }
  .brand-badge {
    width: 58px; height: 20px; border-radius: 3px;
    background: linear-gradient(180deg, #5a5a5a, #2e2e2e);
    border: 1px solid #7a7a7a;
  }

  .contact-band {
    position: absolute; left: 0; top: 900px; width: 700px; height: 90px;
    background: linear-gradient(90deg, #2a2a2a 0%, #0d0d0d 30%, #6d6d6d 55%, #1a1a1a 70%, #bcbcbc 92%, #ffffff 100%);
  }
  .phone {
    position: absolute; left: 40px; top: 914px;
    display: flex; align-items: center; gap: 18px;
    color: var(--white);
    font-family: "Orbitron", sans-serif; font-weight: 900; font-size: 31px; letter-spacing: 2px;
  }
  .phone svg { width: 32px; height: 32px; }
  .service-area {
    position: absolute; left: 40px; top: 960px;
    color: #e0e0e0; font-weight: 600; font-size: 11.5px; letter-spacing: 0.8px;
  }

  .service-truck {
    position: absolute; left: 383px; top: 862px; width: 304px; height: 106px;
    background: linear-gradient(180deg, #e9e9e9 0%, #ffffff 45%, #c9c9c9 75%, #2c2c2c 100%);
    border-radius: 10px 14px 8px 8px;
  }
</style>
</head>
<body>
  <main class="flyer">
    <svg class="flyer-frame" width="700" height="990" viewBox="0 0 700 990">
      <defs>
        <linearGradient id="chrome" x1="0" y1="0" x2="1" y2="0">
          <stop offset="0" stop-color="#1a1a1a"/>
          <stop offset="0.35" stop-color="#e6e6e6"/>
          <stop offset="0.55" stop-color="#5a5a5a"/>
          <stop offset="0.8" stop-color="#f4f4f4"/>
          <stop offset="1" stop-color="#8a8a8a"/>
        </linearGradient>
        <linearGradient id="snow" x1="0" y1="0" x2="0" y2="1">
          <stop offset="0" stop-color="#e7e9ea"/>
          <stop offset="0.6" stop-color="#d3d6d8"/>
          <stop offset="1" stop-color="#eef0f1"/>
        </linearGradient>
      </defs>
      <rect width="700" height="990" fill="#161616"/>
      <rect width="700" height="150" fill="#0a0a0c"/>
      <polygon points="0,35 358,35 432,138 700,138 700,160 420,160 348,57 0,57" fill="url(#chrome)"/>
      <polygon points="0,404 462,404 512,362 700,362 700,384 522,384 472,426 0,426" fill="url(#chrome)"/>
      <polygon points="0,47 356,47 426,149 700,149 700,372 515,372 465,416 0,416"
               fill="url(#snow)" role="img"
               aria-label="Photo: mobile crane and boom lift parked on a snow-covered job site"/>
    </svg>

    <div class="brand">
      <div class="brand-name">PELL ROVING</div>
      <div class="brand-tagline">MOBILE EQUIPMENT SERVICE &amp; REPAIR</div>
      <div class="emergency">24/7 EMERGENCY SERVICE</div>
    </div>

    <h1 class="headline">REPAIRS HEAVY EQUIPMENT</h1>
    <p class="subline">FROM WATER PUMPS TO EXTREMELY LARGE EXCAVATORS</p>

    <div class="gallery">
      <div class="gallery-item truck" role="img" aria-label="Photo: pickup truck with track conversion in the snow"></div>
      <div class="gallery-item loader" role="img" aria-label="Photo: wheel loader being serviced inside the shop"></div>
      <div class="gallery-item rig" role="img" aria-label="Photo: crawler crane assembly on a desert work site"></div>
    </div>

    <h2 class="services-title"><span class="rule"></span>what we do<span class="rule right"></span></h2>
    <ul class="services row-1">
      <li>Diesel engine repair</li><li>Diagnostics</li><li>Air conditioning repair</li><li>Oil changes</li>
    </ul>
    <ul class="services row-2">
      <li>Mobile equipment Repair</li><li>Hydraulic hoses</li><li>Welding &nbsp;Fabrication</li>
    </ul>
    <ul class="services row-3">
      <li>On site maintenance</li><li>Crane inspections and repair</li>
    </ul>

    <section class="brands">
      <p class="brands-title">Brands we work on</p>
      <div class="brands-row">
        <span class="brand-badge" role="img" aria-label="Equipment brand badge"></span>
        <span class="brand-badge" role="img" aria-label="Equipment brand badge"></span>
        <span class="brand-badge" role="img" aria-label="Equipment brand badge"></span>
        <span class="brand-badge" role="img" aria-label="Equipment brand badge"></span>
        <span class="brand-badge" role="img" aria-label="Equipment brand badge"></span>
      </div>
    </section>

    <div class="contact-band"></div>
    <div class="phone">
      <svg viewBox="0 0 24 24" aria-hidden="true"><path fill="#ffffff" d="M6.6 10.8a15.1 15.1 0 0 0 6.6 6.6l2.2-2.2c.3-.3.7-.4 1-.2 1.1.4 2.3.6 3.6.6.6 0 1 .4 1 1V20c0 .6-.4 1-1 1A17 17 0 0 1 3 4c0-.6.4-1 1-1h3.5c.6 0 1 .4 1 1 0 1.3.2 2.5.6 3.6.1.3 0 .7-.2 1z"/></svg>
      <span>801 362 5817</span>
    </div>
    <p class="service-area">SERVING UTAH · WYOMING · IDAHO · NEVADA</p>
    <div class="service-truck" role="img" aria-label="Photo: white service truck with crane body"></div>
  </main>
</body>
</html>
```